A label for a massage gel with bee venom for chronic pain

The product is a massage gel with natural ingredients that contain beehive products (propolis, bee venom, bee wax) and has an effect similar to Tor Vell.

The product is packed in a 250 ml plastic jar, and we need a proper label.

```html
<!DOCTYPE html>
<html lang="en">
<head>
<meta charset="utf-8">
<title>Hivell Menthol Pain Relieving Gel – Jar Labels</title>
<link rel="stylesheet" href="https://fonts.googleapis.com/css2?family=Exo+2:ital,wght@0,400;0,600;0,800;0,900;1,700;1,800;1,900&family=Roboto+Condensed:wght@400&display=swap">
<style>
  :root{
    --lime:#d6df22;
    --stripe:#8cc63f;
    --red:#e31e26;
    --deep-red:#b3171f;
    --near-black:#1b0b0b;
    --ink:#141414;
    --white:#ffffff;
    --gold:#f2d21a;
  }
  html,body{margin:0;padding:0;width:1200px;height:1200px;overflow:hidden;background:var(--white);}
  .stage{position:absolute;left:0;top:0;width:1530px;height:1530px;transform:scale(0.784);transform-origin:0 0;}
  .label{position:absolute;height:394px;background:var(--lime);overflow:hidden;font-family:"Exo 2",sans-serif;color:var(--ink);}
  .label--front{left:382px;top:38px;width:912px;}
  .label--wrap{left:30px;top:484px;width:1470px;}
  .label svg.backdrop{position:absolute;left:0;top:0;}
  .caption{position:absolute;font-family:"Roboto Condensed",sans-serif;font-size:20px;color:#222;width:400px;text-align:center;}
  .abs{position:absolute;}
  .bee-badge{width:112px;height:110px;border-radius:50%;background:radial-gradient(circle,#f4e04d 0%,#c9c93a 60%,rgba(214,223,34,0) 72%);}
  .ingredients-line{font-size:16px;font-style:italic;font-weight:600;color:#d0202a;white-space:nowrap;}
  .chronic-band{height:44px;background:linear-gradient(90deg,rgba(0,0,0,0) 0%,#111 12%,#222 80%,rgba(40,40,40,0) 100%);}
  .chronic-text{font-size:36px;font-weight:900;font-style:italic;color:var(--white);white-space:nowrap;letter-spacing:.5px;}
  .gel-type{font-size:28px;font-weight:600;white-space:nowrap;}
  .brand-name{font-size:104px;font-weight:900;letter-spacing:-2px;white-space:nowrap;line-height:1;color:var(--ink);}
  .subtitle{font-size:25px;font-weight:800;font-style:italic;white-space:nowrap;letter-spacing:.5px;}
  .claim{font-size:20px;font-weight:700;font-style:italic;text-align:center;line-height:1.15;white-space:nowrap;}
  .volume{font-size:24px;font-weight:400;}
  .runner{border-radius:40% 40% 30% 30%;background:radial-gradient(ellipse at 50% 45%,#2a0606 0%,#551015 55%,rgba(120,20,25,0) 75%);}
  .deep-relief{font-size:24px;font-weight:800;font-style:italic;color:var(--white);line-height:1.05;transform:rotate(-16deg);transform-origin:0 0;white-space:nowrap;}
  .deep-relief--gold{color:var(--gold);font-size:17px;transform:rotate(-15deg);transform-origin:0 100%;}
  .directions{font-family:"Roboto Condensed",sans-serif;font-size:11.5px;line-height:15.4px;text-align:justify;width:268px;color:#222;}
  .directions p{margin:0 0 14px 0;}
  .key-kicker{font-size:16px;font-weight:700;font-style:italic;color:var(--gold);white-space:nowrap;transform:rotate(-15deg);transform-origin:0 100%;line-height:20px;}
  .key-item{font-size:38px;font-weight:900;line-height:44px;color:var(--white);white-space:nowrap;padding:0 40px 4px 0;border-bottom:4px solid var(--red);transform:rotate(-15deg);transform-origin:0 100%;}
</style>
</head>
<body>
<main class="stage">

  <section class="label label--front">
    <svg class="backdrop" width="912" height="394" viewBox="0 0 912 394">
      <defs>
        <radialGradient id="glowA" cx="0.5" cy="0.5" r="0.5">
          <stop offset="0" stop-color="#fff"/><stop offset="0.6" stop-color="#fff" stop-opacity=".95"/><stop offset="1" stop-color="#fff" stop-opacity="0"/>
        </radialGradient>
        <linearGradient id="darkA" x1="0" x2="1"><stop offset="0" stop-color="#b3171f"/><stop offset="1" stop-color="#1b0b0b"/></linearGradient>
      </defs>
      <g fill="#8cc63f" opacity=".8">
        <rect x="40" y="172" width="60" height="6" rx="3"/><rect x="60" y="192" width="40" height="6" rx="3"/>
        <rect x="40" y="212" width="70" height="6" rx="3"/><rect x="56" y="232" width="50" height="6" rx="3"/>
        <rect x="634" y="58" width="50" height="6" rx="3"/><rect x="620" y="78" width="60" height="6" rx="3"/>
        <rect x="640" y="98" width="44" height="6" rx="3"/><rect x="626" y="118" width="56" height="6" rx="3"/>
        <rect x="646" y="138" width="40" height="6" rx="3"/>
      </g>
      <ellipse cx="385" cy="230" rx="290" ry="110" fill="url(#glowA)"/>
      <path d="M636,0 C770,100 780,300 460,394 L912,394 L912,0 Z" fill="#e31e26"/>
      <path d="M690,0 C820,120 810,300 590,394 L912,394 L912,0 Z" fill="url(#darkA)"/>
    </svg>
    <div class="abs bee-badge" style="left:70px;top:30px" role="img" aria-label="Bee illustration with curved Bee Venom lettering"></div>
    <div class="abs ingredients-line" style="left:278px;top:38px">Propolis | Bee Venom | Bee Wax</div>
    <div class="abs chronic-band" style="left:172px;top:66px;width:440px"></div>
    <div class="abs chronic-text" style="left:194px;top:66px">FOR CHRONIC PAIN</div>
    <div class="abs gel-type" style="left:266px;top:120px">NON-GREASY GEL</div>
    <div class="abs brand-name" style="left:160px;top:156px">HIVELL</div>
    <div class="abs subtitle" style="left:172px;top:260px">MENTHOL PAIN RELIEVING GEL</div>
    <div class="abs claim" style="left:172px;top:300px;width:420px">Powerful pain relief from minor arthritis,<br>backache, muscle and joint pain</div>
    <div class="abs volume" style="left:72px;top:340px">250 ml</div>
    <div class="abs runner" style="left:610px;top:14px;width:290px;height:370px" role="img" aria-label="Running figure with highlighted muscles and joints"></div>
    <div class="abs deep-relief" style="left:690px;top:338px">Deep Penetrating<br>Pain Relief</div>
  </section>
  <div class="caption" style="left:563px;top:444px">150mm x 65mm</div>

  <section class="label label--wrap">
    <svg class="backdrop" width="1470" height="394" viewBox="0 0 1470 394">
      <defs>
        <radialGradient id="glowB" cx="0.5" cy="0.5" r="0.5">
          <stop offset="0" stop-color="#fff"/><stop offset="0.6" stop-color="#fff" stop-opacity=".95"/><stop offset="1" stop-color="#fff" stop-opacity="0"/>
        </radialGradient>
        <linearGradient id="darkB" x1="0" x2="1"><stop offset="0" stop-color="#b3171f"/><stop offset="1" stop-color="#1b0b0b"/></linearGradient>
      </defs>
      <g fill="#8cc63f" opacity=".8">
        <rect x="395" y="172" width="60" height="6" rx="3"/><rect x="415" y="192" width="40" height="6" rx="3"/>
        <rect x="395" y="212" width="70" height="6" rx="3"/><rect x="411" y="232" width="50" height="6" rx="3"/>
        <rect x="1000" y="58" width="50" height="6" rx="3"/><rect x="986" y="78" width="60" height="6" rx="3"/>
        <rect x="1006" y="98" width="44" height="6" rx="3"/><rect x="992" y="118" width="56" height="6" rx="3"/>
        <rect x="1012" y="138" width="40" height="6" rx="3"/>
      </g>
      <ellipse cx="740" cy="230" rx="290" ry="110" fill="url(#glowB)"/>
      <path d="M1010,0 C1150,100 1150,300 820,394 L1470,394 L1470,0 Z" fill="#e31e26"/>
      <path d="M1060,0 C1190,120 1180,300 950,394 L1470,394 L1470,0 Z" fill="url(#darkB)"/>
    </svg>
    <div class="abs directions" style="left:70px;top:32px">
      <p>This medication is used to treat minor aches and pains of the muscles/joints (such as arthritis, backache, sprains). Menthol is known as a counterirritant. It works by causing the skin to feel cool and then warm. These feelings on the skin distract you from feeling the aches/pains deeper in your muscles and joints.</p>
      <p>How to use Pain Relief Gel Topical<br>If you are using the over-the-counter product to self-treat, read and follow all directions on the product package before using this medication. If you have any questions, consult your pharmacist. If your doctor has prescribed this medication, use it as directed.</p>
      <p>This medication is for use on the skin only. Apply to the affected area no more than 3 to 4 times a day. If you are using the cream, gel, or liquid, rub in gently and thoroughly. Some liquid forms of this medication should be shaken before use. Check the manufacturer's information for specific directions. Let the medicine dry completely before letting anyone else touch the area.</p>
    </div>
    <div class="abs bee-badge" style="left:425px;top:22px" role="img" aria-label="Bee illustration with curved Bee Venom lettering"></div>
    <div class="abs chronic-band" style="left:527px;top:58px;width:440px"></div>
    <div class="abs chronic-text" style="left:547px;top:58px">FOR CHRONIC PAIN</div>
    <div class="abs gel-type" style="left:618px;top:108px">NON-GREASY GEL</div>
    <div class="abs brand-name" style="left:512px;top:148px">HIVELL</div>
    <div class="abs subtitle" style="left:525px;top:252px">MENTHOL PAIN RELIEVING GEL</div>
    <div class="abs claim" style="left:530px;top:294px;width:420px">Powerful pain relief from minor arthritis,<br>backache, muscle and joint pain</div>
    <div class="abs volume" style="left:485px;top:340px">250 ml</div>
    <div class="abs runner" style="left:960px;top:14px;width:300px;height:370px" role="img" aria-label="Running figure with highlighted muscles and joints"></div>
    <div class="abs key-kicker" style="left:1252px;top:60px">Three Main Ingredients</div>
    <div class="abs key-item" style="left:1253px;top:88px">Propolis</div>
    <div class="abs key-item" style="left:1253px;top:156px">Bee Venom</div>
    <div class="abs key-item" style="left:1253px;top:224px">Bee Wax</div>
    <div class="abs deep-relief deep-relief--gold" style="left:1253px;top:304px">Deep Penetrating<br>Pain Relief</div>
  </section>
  <div class="caption" style="left:563px;top:888px">242mm x 65mm(360)</div>

</main>
</body>
</html>
```